Design a Website Mockup for a Job Search Engine

This design contest is for a Job Search Engine.
Similar to popular job search engines like: [login to view URL], [login to view URL], [login to view URL] and [login to view URL]
I require a modern beautiful design that is not too overpowering but blows the above sites away.
The design must be highly driven toward the perfect user experience with guidance on the correct fonts to be used and search result placement for best visibility.
The pages that i require mocked up:
Homepage, Search Results (check out [login to view URL] or [login to view URL] for the type of data that will be shown on the results page), About page
Please be creative as possible.
The winner will be the mockup that displays the best UX experience with a modern catchy design.
Please note the site will be a responsive design so please also show mockups for tablet and mobile as well as desktop for all above pages.

```html
<!DOCTYPE html>
<html lang="en">
<head>
<meta charset="utf-8">
<title>WorkHarbor – Find a Job</title>
<link rel="stylesheet" href="https://fonts.googleapis.com/css2?family=Source+Sans+3:ital,wght@0,300;0,400;0,600;0,700;0,900;1,400&family=Oswald:wght@500;700&family=Roboto+Condensed:wght@400;700&display=swap">
<style>
:root{
  --yellow:#ffd400;
  --gold:#ffc800;
  --green:#2f8a1f;
  --green-dark:#267318;
  --navy:#0b0b2e;
  --ink:#333;
  --muted:#666;
  --light:#f3f3f3;
  --footer:#242424;
  --footer-deep:#141414;
  --white:#fff;
}
*{box-sizing:border-box;margin:0;padding:0}
html,body{width:1200px;height:2720px;overflow:hidden}
body{font-family:"Source Sans 3",sans-serif;color:var(--ink);background:var(--white)}
.page{position:relative;width:1200px;height:2720px;overflow:hidden}
.abs{position:absolute}

/* hero */
.hero{left:0;top:0;width:1200px;height:523px;background:linear-gradient(100deg,#8b6a58 0%,#c4a58e 22%,#3a3440 38%,#d9d3cc 62%,#f1efec 100%);box-shadow:0 12px 18px rgba(0,0,0,.25)}
.topbar{left:0;top:0;width:1200px;height:29px;background:rgba(30,30,30,.85)}
.topbar a{position:absolute;top:9px;font-size:8px;color:#ddd;text-decoration:none}
.topbar .login{font-weight:700;color:#fff;font-size:9px}
.dot{position:absolute;top:9px;width:9px;height:9px;border-radius:50%;background:#fff}
.navbar{left:0;top:29px;width:1200px;height:51px;background:rgba(45,45,45,.78);border-bottom:3px solid var(--yellow)}
.brand{left:188px;top:44px;font-weight:700;font-size:22px;color:var(--yellow);letter-spacing:.3px}
.nav a{position:absolute;top:50px;font-size:11px;color:#fff;text-decoration:none}
.nav .active{left:469px;top:31px;width:112px;height:49px;background:rgba(70,70,70,.8);color:var(--yellow);text-align:center;line-height:49px;padding:0}
.nav .post{left:892px;top:40px;width:121px;height:29px;background:var(--yellow);color:#111;font-weight:700;font-size:13px;text-align:center;line-height:29px}

.search-card{left:671px;top:133px;width:344px;height:336px;background:rgba(230,230,230,.82);border:2px solid #555}
.search-card h1{position:absolute;left:20px;top:18px;font-size:52px;font-weight:900;color:var(--navy);letter-spacing:-1px;line-height:1}
.search-card label{position:absolute;left:20px;font-size:16px;font-weight:700;color:var(--navy)}
.field{position:absolute;background:#fff;border:1px solid #ddd;font-size:13px;color:#bbb;padding-left:6px;display:flex;align-items:center}
.search-card .field{left:20px;width:299px;height:43px}
.search-btn{left:20px;top:246px;width:299px;height:56px;background:var(--yellow);font-size:23px;font-weight:700;color:#111;display:flex;align-items:center;justify-content:center}

/* intro */
.intro-title{left:0;top:592px;width:1200px;text-align:center;font-size:54px;font-weight:300;color:#333}
.intro-text{left:275px;top:667px;width:650px;text-align:center;font-size:16.5px;line-height:21px;color:#555;font-weight:300}
.tile{top:755px;width:211px;height:165px;color:#fff;text-align:center}
.tile h3{margin-top:20px;font-size:17px;font-weight:700;letter-spacing:.4px}
.tile svg{display:block;margin:18px auto 0}
.tile::after{content:"";position:absolute;left:94px;bottom:-25px;border-left:12px solid transparent;border-right:12px solid transparent;border-top:25px solid var(--tone)}
.tile.green{left:243px;background:var(--green);--tone:var(--green)}
.tile.gold{left:491px;background:var(--gold);--tone:var(--gold)}
.tile.navy{left:739px;background:var(--navy);--tone:var(--navy)}

/* hire band */
.hire{left:0;top:1003px;width:1200px;height:413px;background:var(--light)}
.hire-title{font-family:"Oswald",sans-serif;font-weight:700;color:var(--green);font-size:41px;line-height:39px;text-transform:uppercase;white-space:nowrap}
.hire-label{font-family:"Roboto Condensed",sans-serif;font-weight:700;color:#999;font-size:14px}
.select{position:absolute;background:#fff;border:1px solid #ddd;font-family:"Roboto Condensed",sans-serif;font-size:13px;color:#aaa;padding-left:13px;display:flex;align-items:center}
.select .caret{position:absolute;right:0;top:-1px;width:34px;height:44px;background:var(--green-dark);display:flex;align-items:center;justify-content:center}
.green-btn{position:absolute;background:var(--green);color:#fff;font-family:"Roboto Condensed",sans-serif;font-size:24px;display:flex;align-items:center;justify-content:center}
.or{left:577px;top:1186px;font-family:"Oswald",sans-serif;font-weight:700;font-size:40px;color:#999}
.hire .field{font-family:"Roboto Condensed",sans-serif;padding-left:14px;color:#aaa}

/* resume band */
.resume{left:0;top:1416px;width:1200px;height:448px;background:var(--gold)}
.resume h2{position:absolute;left:191px;top:80px;font-size:54px;font-weight:300;line-height:52px;color:#222}
.resume p{position:absolute;left:188px;top:220px;width:345px;font-size:17.5px;line-height:21.5px;color:#333;font-weight:300}
.resume .btn{position:absolute;left:188px;top:331px;width:233px;height:45px;background:#fff;font-size:19px;color:#333;display:flex;align-items:center;justify-content:center}
.devices{left:560px;top:68px;width:447px;height:267px;background:linear-gradient(135deg,#1c1c1c 0%,#1e7a17 35%,#3da32a 65%,#d9d9d9 100%);border-radius:8px}

/* offer */
.offer{left:0;top:1864px;width:1200px;height:196px;background:var(--light)}
.offer .pct{position:absolute;left:200px;top:60px;font-size:64px;font-weight:700;color:var(--navy);line-height:1}
.offer .pct span{font-weight:300;color:#bbb;font-size:46px;margin-left:14px;letter-spacing:2px}
.offer h4{position:absolute;left:476px;top:56px;font-size:18px;font-weight:400;color:#222}
.offer hr{position:absolute;left:476px;top:82px;width:537px;border:0;border-top:1px solid #ccc}
.offer p{position:absolute;left:476px;top:96px;width:540px;font-size:16px;line-height:21px;color:#555;font-weight:300}

/* members */
.members{left:0;top:2060px;width:1200px;height:433px;background:var(--green);color:#fff;text-align:center}
.members h2{position:absolute;left:0;top:34px;width:1200px;font-size:54px;font-weight:300}
.avatar{left:545px;top:130px;width:134px;height:134px;border-radius:50%;border:4px solid #fff;background:linear-gradient(160deg,#e6d6c8,#a8776a)}
.stars{left:0;top:272px;width:1200px}
.quote{left:290px;top:318px;width:620px;font-size:18px;line-height:22px;font-style:italic;font-family:"Roboto Condensed",sans-serif}
.member-name{left:0;top:375px;width:1200px;font-size:19px;font-weight:700;font-family:"Roboto Condensed",sans-serif}

/* footer */
.footer{left:0;top:2493px;width:1200px;height:187px;background:var(--footer)}
.footer ul{position:absolute;list-style:none;top:62px}
.footer li{font-size:11px;color:#ccc;line-height:19px}
.footer li::before{content:"›";margin-right:9px;color:#999}
.vline{position:absolute;top:47px;width:1px;height:93px;background:#555}
.thumbs{left:456px;top:48px;width:137px;display:grid;grid-template-columns:repeat(3,41px);gap:5px}
.thumbs i{display:block;height:27px;background:#666}
.sub-label{left:871px;top:44px;font-size:9px;color:#ddd}
.sub-input{left:871px;top:62px;width:124px;height:17px;background:#555;border:1px solid #888}
.sub-btn{left:871px;top:86px;width:124px;height:16px;background:var(--yellow);font-size:9px;color:#222;text-align:center;line-height:16px}
.social i{position:absolute;top:121px;width:18px;height:18px;border-radius:50%;background:#fff}
.bottom{left:0;top:2680px;width:1200px;height:40px;background:var(--footer-deep)}
.bottom .brand-sm{position:absolute;left:187px;top:14px;font-size:11px;font-weight:700;color:var(--yellow)}
.bottom .copy{position:absolute;left:259px;top:15px;font-size:8px;color:#ccc}
.bottom a{position:absolute;top:15px;font-size:9px;color:#ccc;text-decoration:none}
</style>
</head>
<body>
<div class="page">

  <section class="hero abs" role="img" aria-label="Photo of a smiling professional woman working at a laptop in a bright office"></section>

  <div class="topbar abs">
    <a style="left:188px">About Us</a><a style="left:233px">Careers</a><a style="left:275px">Services</a>
    <a style="left:316px">Partners</a><a style="left:360px">Contact</a><a style="left:400px">Resources</a>
    <i class="dot" style="left:907px"></i><i class="dot" style="left:926px"></i><i class="dot" style="left:946px"></i>
    <a class="login" style="left:979px">Log In</a>
  </div>
  <header class="navbar abs"></header>
  <div class="brand abs">WORKHARBOR</div>
  <nav class="nav">
    <a class="active">Find a Job</a>
    <a style="left:608px">Find Resumes</a>
    <a style="left:713px">Companies</a>
    <a style="left:803px">How It Works</a>
    <a class="post">Post Job</a>
  </nav>

  <form class="search-card abs">
    <h1>FIND A JOB</h1>
    <label style="top:93px">What</label>
    <div class="field" style="top:112px">job title, keyword or company name</div>
    <label style="top:165px">Where</label>
    <div class="field" style="top:184px">city, postal code, province</div>
    <div class="search-btn abs">Search Job</div>
  </form>

  <h2 class="intro-title abs">Get more from your job search</h2>
  <p class="intro-text abs">Lorem Ipsum is simply dummy text of the printing and typesetting industry. Lorem Ipsum<br>has been the industry's standard dummy text ever since the 1500s</p>

  <div class="tile green abs">
    <h3>CAREER NOTES BLOG</h3>
    <svg width="52" height="66" viewBox="0 0 52 66" fill="none" stroke="#fff" stroke-width="4"><rect x="3" y="8" width="46" height="55" rx="4"/><rect x="16" y="2" width="20" height="10" rx="2" fill="var(--green)"/><path d="M13 26h26M13 36h26M13 46h26"/></svg>
  </div>
  <div class="tile gold abs">
    <h3>LOCAL JOBS</h3>
    <svg width="72" height="68" viewBox="0 0 72 68" fill="#fff"><path d="M2 12 22 2v54L2 66z"/><path d="M26 2l20 10v54L26 56z"/><path d="M50 12 70 2v54l-20 10z"/></svg>
  </div>
  <div class="tile navy abs">
    <h3>COMPANY DIRECTORY</h3>
    <svg width="66" height="66" viewBox="0 0 66 66" fill="none" stroke="#fff" stroke-width="4"><circle cx="33" cy="33" r="29" fill="#fff"/><circle cx="33" cy="33" r="29"/><path d="M33 4c-10 9-10 49 0 58M33 4c10 9 10 49 0 58M4 33h58M9 18h48M9 48h48" stroke="var(--navy)" stroke-width="3"/></svg>
  </div>

  <section class="hire abs">
    <h2 class="hire-title abs" style="left:257px;top:64px">Need a<br>Professional?</h2>
    <div class="hire-label abs" style="left:257px;top:153px">I need a</div>
    <div class="select" style="left:257px;top:170px;width:284px;height:44px">select professional
      <span class="caret"><svg width="14" height="8"><path d="M0 0h14L7 8z" fill="#fff"/></svg></span></div>
    <div class="hire-label abs" style="left:257px;top:224px">in</div>
    <div class="select" style="left:257px;top:242px;width:284px;height:44px">select by city, postal code, province
      <span class="caret"><svg width="14" height="8"><path d="M0 0h14L7 8z" fill="#fff"/></svg></span></div>
    <div class="green-btn" style="left:257px;top:305px;width:284px;height:44px">Search</div>

    <div class="or abs" style="top:183px">OR</div>

    <h2 class="hire-title abs" style="left:662px;top:64px">Post Job Now</h2>
    <div class="field" style="left:660px;top:117px;width:284px;height:43px">Name</div>
    <div class="field" style="left:660px;top:174px;width:284px;height:43px">Email</div>
    <div class="field" style="left:660px;top:233px;width:284px;height:59px;align-items:flex-start;padding-top:14px">Job requirement</div>
    <div class="green-btn" style="left:660px;top:306px;width:284px;height:44px">Post Job</div>
  </section>

  <section class="resume abs">
    <h2>Resume<br>Builder</h2>
    <p>Lorem Ipsum is simply dummy text of the printing and typesetting industry. Lorem Ipsum has been the industry's standard dummy text ever since the 1500s</p>
    <div class="btn">Build Your Resume</div>
    <div class="devices abs" role="img" aria-label="Illustration of the resume builder on a laptop, tablet and phone"></div>
  </section>

  <section class="offer abs">
    <div class="pct">25%<span>OFF</span></div>
    <h4>Special Offer</h4>
    <hr>
    <p>Lorem ipsum dolor sit amet, consectetur adipiscing elit. Integer gravida velit quis dolor tristiqumsan. Pellentesque elit tortor, adipiscing vel velit in, ultricies fermentum nulla. Donec in urna sem. Nulla facilisi.</p>
  </section>

  <section class="members abs">
    <h2>Featured Members</h2>
    <svg class="abs" style="left:229px;top:190px" width="18" height="34"><path d="M18 0v34L0 17z" fill="#fff"/></svg>
    <svg class="abs" style="left:953px;top:190px" width="18" height="34"><path d="M0 0v34l18-17z" fill="#fff"/></svg>
    <div class="avatar abs" role="img" aria-label="Portrait photo of the featured member"></div>
    <svg class="stars abs" width="1200" height="28" viewBox="0 0 1200 28">
      <defs><path id="star" d="M12 0l3.6 8.2 8.9.8-6.8 5.9 2 8.7L12 19l-7.7 4.6 2-8.7L-.5 9l8.9-.8z" fill="#ffd400"/></defs>
      <use href="#star" x="540" y="2"/><use href="#star" x="569" y="2"/><use href="#star" x="598" y="2"/><use href="#star" x="627" y="2"/><use href="#star" x="656" y="2"/>
    </svg>
    <p class="quote abs">“After having a disappointing experience with another company, it is refreshing to<br>work with such a professional team!”</p>
    <p class="member-name abs">Dana Whitfield</p>
  </section>

  <footer class="footer abs">
    <ul style="left:188px"><li>Find A Job</li><li>Find Resume</li><li>Resume Builder</li><li>How It Works</li></ul>
    <ul style="left:327px"><li>Post A Job</li><li>Find Professional</li><li>Companies</li></ul>
    <span class="vline" style="left:431px"></span>
    <div class="thumbs abs"><i></i><i></i><i></i><i></i><i></i><i></i><i></i><i></i><i></i></div>
    <span class="vline" style="left:621px"></span>
    <ul style="left:647px"><li>About Us</li><li>Careers</li><li>Services</li><li>Industries</li></ul>
    <ul style="left:749px"><li>Partners</li><li>Contact</li><li>Resources</li></ul>
    <span class="vline" style="left:829px"></span>
    <div class="sub-label abs">Subscribe to our newsletters</div>
    <div class="sub-input abs"></div>
    <div class="sub-btn abs">Subscribe</div>
    <div class="social"><i style="left:875px"></i><i style="left:916px"></i><i style="left:956px"></i></div>
  </footer>
  <div class="bottom abs">
    <span class="brand-sm">WORKHARBOR</span>
    <span class="copy">Copyrights 2015. All rights reserved</span>
    <a style="left:915px">Register</a>
    <a style="left:969px">Sign In</a>
  </div>

</div>
</body>
</html>
```